Digital Marketing Website Design

I need the homepage designed for my new digital marketing agency I am starting. The main goal for this homepage is to drive people to make an appointment for me to discuss their upcoming projects. Here are some examples of the layouts that I would like to emulate.
https://www.tallmarsh.com/
https://www.quillforge.com/
https://pebblenook.com/
https://drvenholt.com/
https://www.quietlyrooted.org/
My main focus is to attract leads that need help with running digital ads such as Chatterly ads and Finder Promos. I do offer other services like SEO and other things but the main focus is digital Ads.
The final design should communicate Orchid Digital is a Digital marketing strategist building predictable revenue for small businesses through digital ads, email and marketing automation.
Target Market(s)
30-55, business owners, income 100K+, ecommerce companies, etc.
Industry/Entity Type
Digital Marketing
Number of Pages Required
2 page
Font styles to use
Requirements
Must have
- An appealing look and feel set to drive people to make an appointment.
Logo
There needs to be a call to action button in the far right of the navigation
The same call to action in the navigation needs to be in each section on the homepage.
I need the homepage and an about us page.

```html
<!DOCTYPE html>
<html lang="en">
<head>
<meta charset="utf-8">
<title>Orchid Digital — Home</title>
<link rel="stylesheet" href="https://fonts.googleapis.com/css2?family=Archivo:wght@600&family=Lato:wght@400;700&family=Open+Sans:wght@300;400;700&display=swap">
<style>
  :root {
    --brand-red: #e8352f;
    --brand-orange: #e0852a;
    --ink: #2b2b2b;
    --nav-text: #333333;
    --white: #ffffff;
    --band-grey: #f6f6f6;
    --hero-dark: #060403;
    --logo-ink: #1b1b1b;
  }
  * { box-sizing: border-box; margin: 0; padding: 0; }
  html, body {
    width: 1200px; height: 1007px; overflow: hidden;
    background: var(--band-grey);
    font-family: "Open Sans", sans-serif;
  }
  .page { position: relative; width: 1200px; height: 1007px; }

  /* Navigation */
  .site-nav {
    position: absolute; top: 0; left: 0; right: 0; height: 64px;
    background: var(--white);
    display: flex; align-items: center; justify-content: space-between;
    padding: 0 110px 0 112px; z-index: 2;
  }
  .brand { display: flex; align-items: center; gap: 8px; }
  .brand-mark { width: 14px; height: 14px; background: var(--brand-red); }
  .brand-name {
    font-family: "Archivo", sans-serif; font-weight: 600;
    font-size: 21px; letter-spacing: -0.5px; color: var(--brand-red);
    text-transform: uppercase;
  }
  .nav-links { display: flex; align-items: center; gap: 22px; list-style: none; }
  .nav-links a {
    font-family: "Lato", sans-serif; font-size: 15px; color: var(--nav-text);
    text-decoration: none;
  }
  .nav-links a.is-current { color: var(--brand-red); }
  .nav-cta {
    font-family: "Lato", sans-serif; font-size: 12px; font-weight: 700;
    color: var(--brand-red); text-decoration: none; text-transform: uppercase;
    border: 1px solid var(--brand-red); padding: 9px 12px; margin-left: 2px;
  }

  /* Hero */
  .hero {
    position: absolute; top: 64px; left: 0; width: 1200px; height: 620px;
    clip-path: polygon(0 0, 100% 0, 100% 91%, 0 100%);
    color: var(--white); text-align: center;
  }
  .hero-photo {
    position: absolute; inset: 0;
    background:
      radial-gradient(ellipse 300px 420px at 560px 300px, rgba(150,80,25,0.55), transparent 70%),
      radial-gradient(ellipse 380px 300px at 330px 470px, rgba(120,60,20,0.45), transparent 70%),
      radial-gradient(ellipse 260px 320px at 880px 220px, rgba(90,45,15,0.4), transparent 70%),
      var(--hero-dark);
  }
  .hero-content { position: relative; padding-top: 122px; }
  .hero-title {
    font-family: "Archivo", sans-serif; font-weight: 600;
    font-size: 43px; line-height: 84px; letter-spacing: -0.3px;
    text-transform: uppercase;
  }
  .hero-lede {
    margin: 26px auto 0; width: 660px;
    font-weight: 300; font-size: 22px; line-height: 42px; letter-spacing: 0.4px;
  }
  .hero-actions {
    margin-top: 42px; display: flex; justify-content: center; align-items: center; gap: 62px;
  }
  .hero-link {
    font-weight: 700; font-size: 14px; color: var(--brand-orange);
    text-decoration: none; text-transform: uppercase; letter-spacing: 0.4px;
  }
  .hero-button {
    background: var(--brand-red); color: var(--white);
    font-weight: 700; font-size: 14px; text-transform: uppercase; letter-spacing: 0.4px;
    text-decoration: none; padding: 15px 27px;
  }

  /* Client band */
  .clients {
    position: absolute; top: 760px; left: 0; right: 0; height: 130px;
    display: flex; align-items: center; justify-content: center; gap: 0;
  }
  .carousel-arrow { width: 40px; display: flex; justify-content: center; }
  .client-list { display: flex; list-style: none; width: 900px; justify-content: space-between; align-items: center; }
  .client {
    width: 170px; display: flex; align-items: center; justify-content: center; gap: 8px;
    font-family: "Open Sans", sans-serif; font-weight: 700; font-size: 19px;
    color: var(--logo-ink); letter-spacing: 1.5px;
  }
  .client-square { width: 16px; height: 16px; background: var(--logo-ink); }
  .client-circle { width: 16px; height: 16px; border-radius: 50%; background: var(--logo-ink); }
</style>
</head>
<body>
<div class="page">
  <header class="site-nav">
    <div class="brand">
      <span class="brand-mark"></span>
      <span class="brand-name">Orchid Digital</span>
    </div>
    <ul class="nav-links">
      <li><a href="#" class="is-current">Home</a></li>
      <li><a href="#">About us</a></li>
      <li><a href="#">Services</a></li>
      <li><a href="#">Resources</a></li>
      <li><a href="#" class="nav-cta">Schedule Appointment</a></li>
    </ul>
  </header>

  <section class="hero">
    <div class="hero-photo" role="img" aria-label="Dark background photograph of glowing flames"></div>
    <div class="hero-content">
      <h1 class="hero-title">We built profitable ad campaigns<br>for small businesses</h1>
      <p class="hero-lede">The selling system that brings in Predictable revenue through digital ads, email, and marketing automation.</p>
      <div class="hero-actions">
        <a href="#" class="hero-link">Free Chatterly Ads Checklist</a>
        <a href="#" class="hero-button">Schedule an Appointment</a>
      </div>
    </div>
  </section>

  <section class="clients" aria-label="Clients">
    <div class="carousel-arrow">
      <svg width="14" height="22" viewBox="0 0 14 22"><path d="M10 3 L3 11 L10 19" fill="none" stroke="#333" stroke-width="2.2"/></svg>
    </div>
    <ul class="client-list">
      <li class="client"><span class="client-circle"></span>BRUSHWELL</li>
      <li class="client">Linnea Ortiz</li>
      <li class="client"><span class="client-square"></span>MIREL</li>
      <li class="client"><span class="client-square"></span>NORVANE</li>
      <li class="client">KESTREL CO</li>
    </ul>
    <div class="carousel-arrow">
      <svg width="14" height="22" viewBox="0 0 14 22"><path d="M4 3 L11 11 L4 19" fill="none" stroke="#333" stroke-width="2.2"/></svg>
    </div>
  </section>
</div>
</body>
</html>
```